New world-class investment firm needs a business card design

We need a business card design for a new investment firm called 'Vallin Soeurs & Company.' We acquire companies in the media sector and secure funding from conservative ultra, high-net worth individuals. We would like a black and white color design. We are seeking classic, elegant, and sophisticated designs. The final design should communicate financial safety, class, timelessness, and highly ethical. On the back of the business card, we would simply like the lion logo to be centered. I have attached a mock card, and variations on it are welcomed.
Conservative
- Garamond

```html
<!DOCTYPE html>
<html lang="en">
<head>
<meta charset="utf-8">
<title>Vallin Soeurs &amp; Company — Business Card</title>
<link rel="stylesheet" href="https://fonts.googleapis.com/css2?family=Open+Sans:wght@400;700&display=swap">
<style>
  :root {
    --backdrop: #d9d9d9;
    --card: #ffffff;
    --ink: #111111;
    --ink-soft: #333333;
    --rule: #8a8a8a;
    --shadow: rgba(0, 0, 0, 0.18);
  }
  * { margin: 0; padding: 0; box-sizing: border-box; }
  html, body {
    width: 1200px;
    height: 900px;
    overflow: hidden;
    background: var(--backdrop);
    font-family: "Open Sans", Verdana, sans-serif;
    color: var(--ink);
  }
  .canvas {
    width: 1200px;
    height: 900px;
    display: flex;
    flex-direction: column;
    align-items: center;
    justify-content: center;
    gap: 60px;
  }
  .card {
    width: 560px;
    height: 320px;
    background: var(--card);
    box-shadow: 0 6px 18px var(--shadow);
    position: relative;
  }

  /* Back side */
  .card-back .mark {
    position: absolute;
    left: 50%;
    top: 58px;
    transform: translateX(-50%);
  }
  .card-back .wordmark {
    position: absolute;
    right: 44px;
    bottom: 40px;
    font-size: 13px;
    font-weight: 400;
    letter-spacing: 0.55em;
    color: var(--ink);
  }

  /* Front side */
  .card-front {
    display: flex;
    flex-direction: column;
    align-items: center;
    padding-top: 26px;
    text-align: center;
  }
  .card-front .mark { margin-bottom: 8px; }
  .company-name {
    font-size: 20px;
    font-weight: 700;
    line-height: 1.1;
  }
  .company-offices {
    font-size: 12px;
    color: var(--ink-soft);
    line-height: 1.4;
  }
  .divider {
    width: 300px;
    height: 1px;
    background: var(--rule);
    margin: 7px 0 8px;
  }
  .person-name {
    font-size: 18px;
    font-weight: 700;
    line-height: 1.15;
  }
  .person-title {
    font-size: 12px;
    color: var(--ink-soft);
    margin-bottom: 8px;
  }
  .contact-email { font-size: 13px; line-height: 1.35; }
  .contact-phone { font-size: 15px; line-height: 1.35; }
</style>
</head>
<body>
  <main class="canvas">
    <section class="card card-back" aria-label="Card back">
      <svg class="mark" width="150" height="150" viewBox="0 0 150 150" aria-hidden="true">
        <circle cx="75" cy="75" r="72" fill="none" stroke="var(--ink)" stroke-width="3"/>
      </svg>
      <p class="wordmark">Vallin Soeurs &amp; Company</p>
    </section>

    <section class="card card-front" aria-label="Card front">
      <svg class="mark" width="66" height="66" viewBox="0 0 66 66" aria-hidden="true">
        <circle cx="33" cy="33" r="31" fill="none" stroke="var(--ink)" stroke-width="2"/>
      </svg>
      <h1 class="company-name">Vallin Soeurs &amp; Company</h1>
      <p class="company-offices">New York • Los Angeles • Geneva</p>
      <div class="divider"></div>
      <h2 class="person-name">Julien A. Vallin</h2>
      <p class="person-title">Chairman &amp; CEO</p>
      <p class="contact-email">julien@vallinsoeurs.com</p>
      <p class="contact-phone">212.555.0147</p>
    </section>
  </main>
</body>
</html>
```